Website for legal services (estates law) called TKV ESTATES LAW

Simple, catchy and easy to use. I am providing estates legal services and I want clients to feel a warm, friendly but professional vibe when they visit my website. I don't want harsh legal pictures (like a picture of a tough lawyer, or pictures of scales of justice). Pictures of books, plants, signing documents or a comfortable looking office are acceptable.

Please use wordpress to design it because I want ability to upload blogs on my own through wordpress after. I am attaching my logo.

Target Market(s)

Millenials, boomers, people in their 40's and anyone looking to transfer property titles or create a will, or anyone whose relatives have died and need help with estates administration.

Industry/Entity Type

Law Firm

Coding

Coded - Design and coding required

Number of Pages Required

4 page

Font styles to use
Sans Serif

Colors
0493ce
33a6d7
85cae6
cee9f5
f4fafd

Requirements
Must have
• - Must be designed with WordPress
- Must have a warm, friendly, professional vibe
- I want to be able to edit any of the content of the website myself
Nice to have
• Pictures of law books, plants, signing documents or a comfortable looking office are acceptable.
Should not have
• I don't want harsh legal pictures (like a picture of a tough lawyer, or pictures of scales of justice).

```html
<!DOCTYPE html>
<html lang="en">
<head>
<meta charset="utf-8">
<title>TKV Estates Law</title>
<link href="https://fonts.googleapis.com/css2?family=Courgette&family=Raleway:wght@300;400;500&display=swap" rel="stylesheet">
<style>
:root{
  --ink:#2b2b2d;
  --text:#3d3e40;
  --muted:#8c8d90;
  --rule:#d6d7d9;
  --dark:#4d4e50;
  --panel:#f0f0f0;
  --card-grey:#e6e6e6;
  --white:#ffffff;
  --footer:#47484a;
  --script:"Courgette", cursive;
  --sans:"Raleway", sans-serif;
}
*{box-sizing:border-box;margin:0;padding:0}
html,body{width:1200px;height:4673px;overflow:hidden}
body{position:relative;background:var(--white);font-family:var(--sans);font-weight:300;color:var(--text)}
.abs{position:absolute}

/* header */
.site-header{position:absolute;left:0;top:0;width:1200px;height:98px;background:#fbfbfb;border-bottom:1px solid #ececec}
.brand{position:absolute;left:91px;top:34px;display:flex;align-items:center;gap:12px;font-family:var(--sans);font-weight:500;font-size:22px;letter-spacing:2px;color:var(--ink)}
.brand-mark{width:20px;height:20px;background:var(--ink)}
.main-nav{position:absolute;top:42px;left:0;width:1200px;font-size:17px;font-weight:400;color:var(--text)}
.main-nav span{position:absolute}

/* hero */
.hero-photo{position:absolute;left:0;top:98px;width:1200px;height:647px;background:linear-gradient(90deg,#e9eef1 0%,#dfe6ea 45%,#c9d2d8 75%,#aeb9c1 100%)}
.hero-frame{position:absolute;left:292px;top:341px;width:596px;height:598px;border:3px solid #ebeced}
.hero-card{position:absolute;left:319px;top:370px;width:542px;height:536px;background:var(--white);text-align:center}
.hero-intro{position:absolute;left:60px;top:116px;width:422px;font-size:19px;line-height:35px;color:var(--ink)}
.hero-quote{position:absolute;left:0;top:302px;width:542px;font-family:var(--script);font-size:34px;line-height:40px;color:var(--ink)}

/* section titles */
.section-title{position:absolute;left:0;width:1200px;text-align:center;font-family:var(--script);font-size:54px;color:#4a4b4d}
.title-rule{position:absolute;height:2px;background:var(--rule)}

/* about */
.about-copy{position:absolute;left:140px;top:1113px;width:920px;text-align:center;font-size:19.5px;line-height:35.5px;color:var(--ink)}
.consult-btn{position:absolute;left:363px;top:1405px;width:424px;height:42px;border:2px solid #9a9b9d;font-size:18px;font-weight:400;letter-spacing:.5px;text-align:center;line-height:38px;color:var(--text)}

/* services */
.services-band{position:absolute;left:0;top:1553px;width:1200px;height:553px;background:var(--dark)}
.services-intro{position:absolute;left:200px;top:1702px;width:800px;text-align:center;font-size:19px;line-height:36px;color:#e6e6e6}
.service-panel{position:absolute;left:100px;top:1883px;width:500px;height:439px;background:var(--panel)}
.service-photo{position:absolute}
.service-name{position:absolute;font-family:var(--sans);font-weight:300;font-size:40px}
.service-rule{position:absolute;height:4px;background:#6a6b6d}
.service-text{position:absolute;font-size:15.5px;line-height:25px}
.service-text ul{list-style:none}
.service-text li{position:relative;padding-left:30px}
.service-text li::before{content:"";position:absolute;left:3px;top:11px;width:4px;height:4px;border-radius:50%;background:currentColor}
.estate-admin{position:absolute;left:141px;top:2378px;width:920px;font-size:15.5px;line-height:25.5px;color:var(--ink)}
.estate-admin ul{list-style:none;margin-top:17px}
.estate-admin li{position:relative;padding-left:38px}
.estate-admin li::before{content:"";position:absolute;left:12px;top:11px;width:4px;height:4px;border-radius:50%;background:var(--ink)}
.realestate-panel{position:absolute;left:600px;top:2690px;width:500px;height:439px;background:var(--dark);color:#eeeeee}

/* blog */
.post-card{position:absolute;top:3368px;width:322px;height:301px;border:1px solid #eeeeee;background:var(--white)}
.post-card.is-featured{background:var(--card-grey);border-color:var(--card-grey)}
.post-date{position:absolute;left:25px;top:32px;font-size:12.5px;font-weight:400;letter-spacing:.5px;color:var(--muted)}
.post-title{position:absolute;left:25px;top:66px;width:270px;font-size:25px;line-height:32px;color:#6a6b6d}
.post-excerpt{position:absolute;left:28px;top:155px;width:270px;font-size:15px;line-height:27px;color:#9a9b9d}
.post-rule{position:absolute;left:170px;top:262px;width:109px;height:1px;background:#bfc0c2}

/* contact */
.map-area{position:absolute;left:0;top:4175px;width:1200px;height:456px;background:linear-gradient(180deg,#e4e7ea 0%,#d8dce0 100%)}
.contact-frame{position:absolute;left:286px;top:3856px;width:595px;height:516px;background:var(--white);border:4px solid #efefef}
.field{position:absolute;left:346px;width:472px;border:2px solid #a9aaac;background:var(--white);font-size:15px;font-weight:400;color:#a4a5a7;padding:4px 14px}
.send-btn{position:absolute;left:346px;top:4128px;width:167px;height:36px;border:2px solid #707173;text-align:center;line-height:32px;font-size:15px;font-weight:500;letter-spacing:1px;color:var(--ink)}
.contact-info{position:absolute;top:4257px;font-size:19px;line-height:24.5px;color:var(--ink)}
.site-footer{position:absolute;left:0;top:4631px;width:1200px;height:42px;background:var(--footer);text-align:center;line-height:42px;font-size:11px;color:#b8b9bb}
</style>
</head>
<body>

<header class="site-header">
  <div class="brand"><span class="brand-mark"></span>TKV ESTATES LAW</div>
  <nav class="main-nav">
    <span style="left:582px">HOME</span>
    <span style="left:680px">ABOUT</span>
    <span style="left:785px">SERVICES</span>
    <span style="left:914px">BLOG</span>
    <span style="left:1008px">CONTACT</span>
  </nav>
</header>

<div class="hero-photo" role="img" aria-label="Soft light photograph of a stack of books on a pale desk"></div>
<div class="hero-frame"></div>
<section class="hero-card">
  <p class="hero-intro">Thank you for visiting TKV Estates Law, where I endeavor to earn your trust and provide you with high quality estates and real estate law services.</p>
  <p class="hero-quote">My goal is to make you<br>feel comfortable<br>as soon as you step foot<br>in my office.</p>
</section>

<!-- about -->
<div class="title-rule" style="left:306px;top:1053px;width:182px"></div>
<h2 class="section-title" style="top:1015px">About</h2>
<div class="title-rule" style="left:709px;top:1053px;width:177px"></div>
<div class="about-copy">
  <p>My name is Tamsin Kovar and I am an estates and real estate lawyer. I graduated from Northbrook University Faculty of Law and my passion is estates law and real estate law.<br>Prior to entering the legal profession, I obtained my CPA (Chartered Professional Accounting) designation and worked in business and management accounting for many years, where I developed a deeper understanding of money and finances.</p>
  <p style="margin-top:35px">As a lawyer, I lean on this foundation frequently for the benefit of my clients.</p>
</div>
<div class="consult-btn">CONTACT ME FOR FREE CONSULTATION</div>

<!-- services -->
<section class="services-band"></section>
<div class="title-rule" style="left:299px;top:1646px;width:154px;background:#6c6d70"></div>
<h2 class="section-title" style="top:1608px;color:#7d7e81">Services</h2>
<div class="title-rule" style="left:721px;top:1646px;width:160px;background:#6c6d70"></div>
<div class="services-intro">
  <p>I use my accounting background to provide a high quality legal experience for my estates and real estate clients.</p>
  <p style="margin-top:4px">Here are the services I provide:</p>
</div>

<article class="service-panel">
  <h3 class="service-name" style="left:50px;top:50px;color:var(--ink)">Estates Law</h3>
  <div class="service-rule" style="left:50px;top:111px;width:271px"></div>
  <div class="service-text" style="left:50px;top:172px;width:430px;color:var(--ink)">
    <p>I offer the following services<br>as part of an estate plan:</p>
    <ul style="margin-top:18px">
      <li>Wills (personal, corporate, foreign property);</li>
      <li>Trusts;</li>
      <li>Powers of Attorney for Personal Care and Property;</li>
      <li>Asset planning to minimize income tax and estate administration tax upon your passing.</li>
    </ul>
  </div>
</article>
<div class="service-photo" style="left:600px;top:1883px;width:500px;height:439px;background:linear-gradient(135deg,#c9a77a 0%,#e8dccb 40%,#f1f1f3 70%,#dfe0e4 100%)" role="img" aria-label="Photograph of a fountain pen and reading glasses resting on a last will document"></div>

<div class="estate-admin">
  <p>I help administer entire estates including:</p>
  <ul>
    <li>Guide the executor with the administration of an entire estate;</li>
    <li>Apply for the Certificate of Appointment of Estate Trustee with/without a Will (Applying for Probate);</li>
    <li>Administer trusts;</li>
    <li>Provide guidance about the requirements of financial institutions, the government, the courts;</li>
    <li>Draft documents required in dealing with various institutions;</li>
    <li>Applying for the Canada Pension Plan Death Benefit;</li>
    <li>Applying for the Estate Information Return.</li>
  </ul>
</div>

<div class="service-photo" style="left:100px;top:2690px;width:500px;height:439px;background:linear-gradient(90deg,#dcdde0 0%,#f4f4f5 45%,#b9bcc0 80%,#6f7377 100%)" role="img" aria-label="Photograph of white bound books standing on a shelf beside a pen holder"></div>
<article class="realestate-panel">
  <h3 class="service-name" style="left:51px;top:43px;color:#f2f2f2">Real Estates Law</h3>
  <div class="service-text" style="left:51px;top:155px;width:410px">
    <p>I help clients with their residential sales, purchases and property transfer needs. My clients' real estate and estate needs often intersect, and for this reason, I offer the following specialized services:</p>
    <ul style="margin-top:18px">
      <li>Transfers of title to family members or spouses;</li>
      <li>Transfers of title from deceased to survivors;</li>
      <li>Transfers of title to estate trustee for the purposes of selling the estate's real estate asset.</li>
    </ul>
  </div>
</article>

<!-- blog -->
<div class="title-rule" style="left:286px;top:3268px;width:205px"></div>
<h2 class="section-title" style="top:3230px">Blog</h2>
<div class="title-rule" style="left:663px;top:3268px;width:205px"></div>

<article class="post-card" style="left:102px">
  <p class="post-date">APRIL 12, 2020</p>
  <h3 class="post-title">Something New About Real Estate Law</h3>
  <p class="post-excerpt">Lorem ipsum dolor sit amet, consectetuer adipiscing elit, sed diam nonummy nibh euismod</p>
  <div class="post-rule"></div>
</article>
<article class="post-card" style="left:439px">
  <p class="post-date" style="top:38px">APRIL 12, 2020</p>
  <h3 class="post-title" style="top:72px">Something New About Real Estate Law</h3>
  <p class="post-excerpt" style="top:161px">Lorem ipsum dolor sit amet, consectetuer adipiscing elit, sed diam nonummy nibh euismod</p>
  <div class="post-rule" style="top:268px"></div>
</article>
<article class="post-card is-featured" style="left:774px">
  <p class="post-date" style="top:42px">APRIL 12, 2020</p>
  <h3 class="post-title" style="top:76px">Something New About Real Estate Law</h3>
  <p class="post-excerpt" style="top:165px">Lorem ipsum dolor sit amet, consectetuer adipiscing elit, sed diam nonummy nibh euismod</p>
  <div class="post-rule" style="top:272px"></div>
</article>

<!-- contact -->
<div class="map-area" role="img" aria-label="Street map of the office neighbourhood"></div>
<section class="contact-frame"></section>
<div class="field" style="top:3895px;height:33px">Name</div>
<div class="field" style="top:3939px;height:33px">Your Email</div>
<div class="field" style="top:3983px;height:32px">Phone Number</div>
<div class="field" style="top:4026px;height:91px">Message</div>
<div class="send-btn">SEND</div>
<address class="contact-info" style="left:346px;font-style:normal">4200 Harbour Street,<br>Suite 1207, Toronto<br>ON M4K2B1</address>
<p class="contact-info" style="left:627px">T: 555.014.2231<br>F: 555.014.8820<br>tamsin@tkv-law.ca</p>

<footer class="site-footer">Copyright © TKV Estates Law</footer>

</body>
</html>
```